Professional Consulting Firm Business Card Design

We need a business card design for a new professional consulting firm that specializes in petroleum, health, and financial consulting. We need a design that is trendy but elegant, and one that would make a summit 300 executive feel comfortable using our services. I have attached a logo that needs to be used in the design. I have also attached a photo of a card design that I like.

On the card we need a place for employee name, title, email address, fax number, phone number, mailing address, and website address.

Industry/Entity Type

Financial

Contact Information for Business Card

see attached

Other font styles liked:
• Calibri or your choice

Requirements
Must have
• style
Nice to have
• texture, rounded edges
Should not have
• no solid black cards but black may be used

```html
<!DOCTYPE html>
<html lang="en">
<head>
<meta charset="utf-8">
<title>Ridgeway Consulting — Business Card</title>
<link href="https://fonts.googleapis.com/css2?family=Questrial&family=Open+Sans:wght@400;700&display=swap" rel="stylesheet">
<style>
  :root {
    --stage: #e9e7e4;
    --navy: #134a7a;
    --navy-deep: #0f4475;
    --slate: #5a5b5d;
    --ink: #4a4a4c;
    --paper: #ffffff;
    --dots: #7b7d80;
  }
  * { box-sizing: border-box; margin: 0; padding: 0; }
  html, body { width: 1200px; height: 1000px; overflow: hidden; }
  body {
    background: var(--stage);
    position: relative;
    font-family: "Questrial", "Century Gothic", sans-serif;
  }
  .card {
    position: absolute;
    left: 265px;
    width: 666px;
    height: 397px;
    box-shadow: 0 3px 10px rgba(0,0,0,0.18);
  }
  .card--front { top: 73px; background: var(--paper); }
  .card--back { top: 532px; background: var(--navy-deep); }

  .brand { position: absolute; display: flex; align-items: center; gap: 12px; }
  .brand__mark { width: 30px; height: 30px; background: var(--navy); flex: none; }
  .brand__text { display: flex; flex-direction: column; }
  .brand__name {
    font-size: 34px; letter-spacing: 0.5px; color: var(--navy); line-height: 1;
  }
  .brand__tagline {
    font-family: "Open Sans", Arial, sans-serif; font-weight: 700;
    font-size: 8px; color: var(--navy); margin-top: 6px; letter-spacing: 0.1px;
  }
  .card--front .brand { left: 32px; top: 48px; }
  .card--back .brand { left: 50%; top: 168px; transform: translateX(-50%); }
  .card--back .brand__mark { background: var(--paper); }
  .card--back .brand__name, .card--back .brand__tagline { color: var(--paper); }

  .person { position: absolute; left: 159px; top: 199px; }
  .person__name {
    font-family: "Open Sans", Arial, sans-serif; font-weight: 700;
    font-size: 19px; color: var(--navy); line-height: 1.2;
  }
  .person__title { font-size: 16px; color: var(--ink); margin-top: 1px; }

  .divider { position: absolute; left: 33px; top: 257px; width: 600px; height: 2px; }

  .contact { position: absolute; top: 282px; font-size: 16px; color: var(--ink); line-height: 20px; }
  .contact--phone { left: 159px; }
  .contact--address { left: 443px; }
  .contact__label { color: var(--navy); }

  .band { position: absolute; top: 365px; height: 32px; }
  .band--primary { left: 0; width: 432px; background: var(--navy); }
  .band--secondary { left: 437px; width: 229px; background: var(--slate); }
  .band__web {
    position: absolute; left: 159px; top: 6px; color: var(--paper); font-size: 16px;
  }

  .back__web {
    position: absolute; left: 0; right: 0; top: 350px; text-align: center;
    color: var(--paper); font-size: 15px; letter-spacing: 1.5px;
  }
</style>
</head>
<body>
  <section class="card card--front">
    <div class="brand">
      <span class="brand__mark"></span>
      <div class="brand__text">
        <span class="brand__name">RIDGEWAY CONSULTING</span>
        <span class="brand__tagline">HEALTH, SAFETY, AND FINANCIAL CONSULTING SERVICES</span>
      </div>
    </div>

    <div class="person">
      <p class="person__name">Daniel R. Whitford</p>
      <p class="person__title">Managing Director</p>
    </div>

    <svg class="divider" viewBox="0 0 600 2" aria-hidden="true">
      <line x1="0" y1="1" x2="600" y2="1" stroke="var(--dots)" stroke-width="1.5" stroke-dasharray="1.5 4.5"/>
      <rect x="126" y="0" width="96" height="2" fill="var(--navy)"/>
    </svg>

    <div class="contact contact--phone">
      <p><span class="contact__label">Tel:</span> + 555 010 2030</p>
      <p><span class="contact__label">Fax:</span> + 555 010 2031</p>
      <p>info@ridgewayconsult.com</p>
    </div>
    <div class="contact contact--address">
      <p>418 Alder Ave. Building</p>
      <p>1200 North</p>
      <p>Lakeview Colorado 80099</p>
    </div>

    <div class="band band--primary"><span class="band__web">www.ridgewayconsult.com</span></div>
    <div class="band band--secondary"></div>
  </section>

  <section class="card card--back">
    <div class="brand">
      <span class="brand__mark"></span>
      <div class="brand__text">
        <span class="brand__name">RIDGEWAY CONSULTING</span>
        <span class="brand__tagline">HEALTH, SAFETY, AND FINANCIAL CONSULTING SERVICES</span>
      </div>
    </div>
    <p class="back__web">www.ridgewayconsult.com</p>
  </section>
</body>
</html>
```